****Amazing Solar Energy Company | Needs A Dynamic Website In Wordpress ****

Here at Brevant Solar, our approach is straightforward: we listen, educate, and collaborate. We are a Residential & Commercial solar energy company located in Sanford, FL. OLD TEMP Website https://www.brevantsolar-example.com/

We are looking for a dynamic website design, layout, and code in Wordpress. We will be using a builder (Elementor) post-install so keep that in mind.

IMPORTANT:
Please See brand kit, font type, site map, and even a rough home page. We even have persona targets if needed.

Please review all images and documents uploaded as well

Please rely on your own design with the goal to educate the consumer on the many benefits of solar energy.

Target Market(s)

Home Owners who are looking for Solar Panels

Industry/Entity Type

Solar Energy, Solar Panels, Green Energy

Coding

Coded - Design and coding required

Number of Pages Required

5+ page

Font styles to use
Other font styles liked:
• Header: Raleway Body Text: Montserrat

Colors

Designer to choose colors to be used in the design.

Requirements
Must have
• Must follow the brand kit color, fonts etc | Must be clean and engaging | Modern, Simplistic, Impact, Clean, Cooling, Calming
Nice to have
• Rotating Header, Step By Steps Visuals

```html
<!DOCTYPE html>
<html lang="en">
<head>
<meta charset="utf-8">
<title>Brevant Solar</title>
<link href="https://fonts.googleapis.com/css2?family=Montserrat:wght@300;400;500;600;700;800&family=Raleway:wght@600;700&display=swap" rel="stylesheet">
<style>
:root{
  --navy:#0a0e30;
  --ink:#14213d;
  --orange:#d4813f;
  --yellow:#fbb80f;
  --slate:#c3ccd2;
  --slate-dark:#aeb8bf;
  --footer:#2b241f;
  --card:#fbf7f4;
  --muted:#555b66;
  --white:#ffffff;
}
*{margin:0;padding:0;box-sizing:border-box}
html,body{width:1200px;height:3058px;overflow:hidden}
body{position:relative;font-family:'Montserrat',sans-serif;color:var(--ink);background:var(--white)}
.abs{position:absolute}
/* header */
.site-header{position:absolute;left:0;top:0;width:1200px;height:72px;background:var(--white)}
.brand{left:58px;top:20px;display:flex;align-items:center;gap:8px;font-weight:700;font-size:22px;letter-spacing:3px;color:var(--ink);white-space:nowrap}
.brand .dot{width:14px;height:14px;border-radius:50%;background:var(--yellow)}
.site-header .brand{top:26px;font-size:16px;letter-spacing:1.5px;gap:7px}
.site-header .brand .dot{width:11px;height:11px}
.nav a{position:absolute;top:31px;font-size:12px;font-weight:500;color:var(--ink);text-decoration:none;white-space:nowrap}
.social{position:absolute;top:21px;width:32px;height:32px;border:2px solid var(--ink);border-radius:50%}
.call{left:1000px;top:14px;color:var(--yellow);font-size:16px;font-weight:500}
.call strong{display:block;color:var(--ink);font-size:21px;font-weight:700;margin-top:2px;letter-spacing:.5px}
/* hero */
.hero{position:absolute;left:0;top:72px;width:1200px;height:708px;background:var(--navy);overflow:hidden}
.hero h1{position:absolute;left:57px;top:66px;font-size:44px;line-height:54px;font-weight:700;color:var(--white)}
.hero .lead{left:57px;top:190px;width:340px;font-size:11px;line-height:19px;font-weight:600;color:var(--white)}
.btn-pill{left:57px;top:266px;width:121px;height:38px;border:1.5px solid var(--yellow);border-radius:20px;color:var(--yellow);font-size:12px;font-weight:600;display:flex;align-items:center;justify-content:center}
.hero .copy{left:57px;top:360px;width:330px;font-size:12px;line-height:19px;font-weight:300;color:#aab0c4}
.btn-box{left:57px;top:451px;width:121px;height:39px;border:1.5px solid #d8dbe4;color:#d8dbe4;font-size:12px;font-weight:600;display:flex;align-items:center;justify-content:center;gap:8px}
.checks{left:57px;top:519px;color:#c6cad4;font-size:12px;font-weight:500}
.checks li{list-style:none;display:flex;align-items:center;gap:8px;height:27px}
.hero-badge{left:525px;top:74px;width:93px;height:92px;background:var(--yellow);border-radius:6px;padding:54px 8px 0;font-size:8px;font-weight:600;color:var(--white);line-height:11px}
.hero-visual{left:606px;top:-6px;width:582px;height:582px;border-radius:50%;border:5px solid var(--white);background:radial-gradient(circle at 50% 40%,#2fae6d 0%,#17584f 30%,#0c2a44 62%,#081233 100%)}
.hero-hands{left:600px;top:560px;width:520px;height:80px;background:linear-gradient(90deg,#0e2640,#3c7ea0,#0e2640);border-radius:50% 50% 0 0;opacity:.8}
.hero-wave{left:0;top:600px}
.dots{left:566px;top:797px;display:flex;gap:6px}
.dots span{width:11px;height:11px;border-radius:50%;background:#c9c9c9}
.dots span:first-child{background:var(--ink)}
/* learning */
.learn-top{left:48px;top:820px}
.eyebrow{left:0;width:1218px;text-align:center;top:900px;font-size:10px;color:var(--orange);font-weight:500}
.learn-title{left:0;width:1218px;text-align:center;top:917px;font-size:34px;font-weight:600;letter-spacing:.5px;color:var(--ink)}
.hub{left:437px;top:1071px;width:320px;height:320px;border-radius:50%;background:linear-gradient(160deg,#5b6670,#2f3a44 55%,#3e4a55);box-shadow:0 8px 14px rgba(0,0,0,.35)}
.hub-name{left:437px;top:1206px;width:320px;text-align:center;color:var(--white)}
.hub-name b{display:block;font-size:22px;font-weight:700;letter-spacing:.5px}
.hub-name span{display:block;font-size:17px;font-weight:600;margin-top:2px}
.node{position:absolute;width:94px;height:94px;border-radius:50%;background:var(--yellow);box-shadow:0 4px 8px rgba(0,0,0,.2);display:flex;align-items:center;justify-content:center}
.ring{position:absolute;width:16px;height:16px;border:2px solid #777;border-radius:50%;background:var(--white)}
.topic h3{font-size:15px;font-weight:600;color:var(--ink);margin-bottom:8px;font-family:'Montserrat',sans-serif}
.topic p{font-size:9.5px;line-height:19px;color:#333}
.topic{position:absolute;width:250px}
.topic.l{text-align:right}
.learn-bottom{left:48px;top:1505px}
/* systems */
.systems{position:absolute;left:50px;top:1618px;width:1090px;height:580px;background:var(--slate);overflow:hidden}
.map{left:10px;top:174px;width:806px;height:404px;background:radial-gradient(ellipse at 45% 45%,var(--slate-dark),var(--slate) 75%);border-radius:40% 45% 30% 35%}
.tag-line{left:83px;top:56px;font-size:8px;font-weight:600}
.systems h2{position:absolute;left:83px;top:75px;font-size:29px;line-height:47px;font-weight:700;color:#111}
.systems .intro{left:570px;top:51px;width:410px;font-size:11.5px;line-height:24px;color:#222}
.btn-dark{left:570px;top:171px;width:213px;height:38px;background:var(--ink);color:var(--white);font-size:16px;font-weight:600;display:flex;align-items:center;justify-content:center;gap:6px}
.stat{left:784px;width:200px;font-size:10px;line-height:16px;color:#222}
.stat b{font-size:13px;font-weight:500}
.stat small{font-size:5px}
/* blog */
.card{position:absolute;top:2225px;width:347px;height:558px;background:var(--card);border-radius:30px;box-shadow:0 4px 10px rgba(0,0,0,.18)}
.card .meta{position:absolute;left:25px;top:50px;font-size:9px;color:#333}
.card .meta span{margin-left:14px}
.card h4{position:absolute;left:25px;top:69px;font-size:13.5px;font-weight:600;color:#111}
.card .sub{position:absolute;left:25px;top:95px;width:240px;font-size:13.5px;line-height:19px;color:#222}
.card .photo{position:absolute;left:25px;top:166px;width:299px;height:203px;background:linear-gradient(180deg,#9db0c2 0%,#5f6a78 45%,#7d8079 100%);box-shadow:0 3px 6px rgba(0,0,0,.3)}
.card .photo.wide{left:19px;top:154px;width:309px;height:215px;background:linear-gradient(180deg,#8fb3d6 0%,#5d7a4a 45%,#23303c 100%)}
.card .chip{position:absolute;left:25px;top:362px;background:var(--yellow);color:var(--white);font-size:7.5px;padding:3px 12px;border-radius:8px}
.card .body{position:absolute;left:25px;top:408px;width:220px;font-size:7.5px;line-height:16px;color:#444}
.card .more{position:absolute;left:50px;top:497px;width:88px;height:26px;background:var(--ink);color:var(--white);font-size:8px;display:flex;align-items:center;justify-content:center;gap:4px}
.card .more i{width:8px;height:8px;border-radius:50%;background:var(--white);display:inline-block}
/* footer */
.site-footer{position:absolute;left:0;top:2813px;width:1200px;height:245px;background:var(--footer);color:#ddd}
.site-footer .brand{left:57px;top:60px;color:#3c8d95}
.foot-about{left:57px;top:125px;width:200px;font-size:9.5px;line-height:17px}
.site-footer h5{position:absolute;top:45px;font-size:9.5px;font-weight:600;color:var(--white)}
.contact{left:404px;font-size:9px;line-height:15px;white-space:nowrap}
.post{left:686px;display:flex;gap:10px;align-items:center;font-size:9px}
.thumb{background:linear-gradient(160deg,#8aa2b8,#4b5866);border:2px solid #eee}
.post b{display:block;color:var(--white);font-weight:600;font-size:9px}
.post small{font-size:8px;color:#ccc}
</style>
</head>
<body>

<header class="site-header">
  <div class="abs brand"><span class="dot"></span>BREVANT SOLAR</div>
  <nav class="nav">
    <a style="left:249px">HOME</a>
    <a style="left:325px">ABOUT US</a>
    <a style="left:425px">WHY CHOOSE US</a>
    <a style="left:574px">SERVICE</a>
    <a style="left:660px">BLOG</a>
    <a style="left:724px">CONTACT US</a>
  </nav>
  <span class="social" style="left:823px"></span>
  <span class="social" style="left:864px"></span>
  <span class="social" style="left:905px"></span>
  <span class="social" style="left:946px"></span>
  <div class="abs call">Call Today!<strong>407-555-0186</strong></div>
</header>

<section class="hero">
  <h1>CLEARLY ENEGY<br>DATA INSIGHTS</h1>
  <p class="abs lead">Lorem ipsum dolor sit amet, consectetur adipiscing elit. Proin integer ornare consectetur sodales</p>
  <div class="abs btn-pill">GET STARTED</div>
  <p class="abs copy">Lorem ipsum dolor sit amet, consectetur adipiscing elit. Proin integer ornare consectetur sodales.Lorem ipsum dolor sit amet, consectetur adipiscing elit. Proin integer ornare consectetur sodales</p>
  <div class="abs btn-box">READ MORE
    <svg width="14" height="10" viewBox="0 0 14 10"><path d="M0 5h12M8 1l4 4-4 4" stroke="#d8dbe4" stroke-width="1.5" fill="none"/></svg></div>
  <ul class="abs checks">
    <li><svg width="12" height="12" viewBox="0 0 12 12"><circle cx="6" cy="6" r="6" fill="#c6cad4"/><path d="M3 6l2 2 4-4" stroke="#0a0e30" stroke-width="1.5" fill="none"/></svg>Reliability, performance, just manufacturing</li>
    <li><svg width="12" height="12" viewBox="0 0 12 12"><circle cx="6" cy="6" r="6" fill="#c6cad4"/><path d="M3 6l2 2 4-4" stroke="#0a0e30" stroke-width="1.5" fill="none"/></svg>Solor Material Financing, energy output</li>
  </ul>
  <div class="abs hero-visual" role="img" aria-label="Glowing light bulb with a green tree and rising bar chart inside, set among stars"></div>
  <svg class="abs hero-wave" width="1200" height="108" viewBox="0 0 1200 108"><path d="M0 50 C200 0 420 70 700 70 C900 70 1100 40 1200 0 L1200 108 L0 108Z" fill="#173a4e"/></svg>
  <div class="abs hero-hands" role="img" aria-label="Low-poly glowing hands holding the bulb"></div>
  <div class="abs hero-badge">The Solar<br>Energy!</div>
</section>

<div class="abs dots"><span></span><span></span><span></span></div>

<svg class="abs learn-top" width="1092" height="82" viewBox="0 0 1092 82"><rect width="1092" height="82" fill="#fff"/><path d="M0 0H1092V70 C800 10 300 10 0 70Z" fill="#0e1a3a"/><path d="M0 70 C300 10 800 10 1092 70 L1092 78 C800 30 300 30 0 78Z" fill="#d4813f"/></svg>
<div class="abs eyebrow">SOLAR PATIOS CONSULTING</div>
<h2 class="abs learn-title">SOLOAR LEARNING CENTER</h2>

<svg class="abs" style="left:340px;top:990px" width="520" height="470" viewBox="0 0 520 470"><ellipse cx="260" cy="240" rx="245" ry="228" fill="none" stroke="#888" stroke-width="2" stroke-dasharray="5 5"/></svg>
<span class="ring" style="left:367px;top:1159px"></span>
<span class="ring" style="left:372px;top:1320px"></span>
<span class="ring" style="left:822px;top:1159px"></span>
<span class="ring" style="left:818px;top:1320px"></span>

<div class="abs hub" role="img" aria-label="Grey house with dark solar panels on the roof"></div>
<div class="abs hub-name"><b>BREVANT SOLAR</b><span>AND STRUCTURES</span></div>

<div class="node" style="left:357px;top:1039px"><svg width="44" height="44" viewBox="0 0 44 44" fill="none" stroke="#fff" stroke-width="2.5"><rect x="6" y="10" width="28" height="14"/><path d="M20 24v12M12 36h16M6 17h28M15 10v14M25 10v14"/></svg></div>
<div class="node" style="left:303px;top:1197px"><svg width="44" height="44" viewBox="0 0 44 44" fill="none" stroke="#fff" stroke-width="2.5"><path d="M6 18L22 6l16 12"/><rect x="10" y="18" width="24" height="18"/><path d="M24 22l-5 7h6l-5 7" /></svg></div>
<div class="node" style="left:376px;top:1360px"><svg width="44" height="44" viewBox="0 0 44 44" fill="none" stroke="#fff" stroke-width="2.5"><circle cx="22" cy="14" r="6"/><path d="M22 2v4M22 22v18M12 30c4 0 10 2 10 8M32 30c-4 0-10 2-10 8"/></svg></div>
<div class="node" style="left:733px;top:1045px"><svg width="44" height="44" viewBox="0 0 44 44" fill="none" stroke="#fff" stroke-width="2.5"><path d="M22 4l14 6v10c0 10-7 16-14 20C15 36 8 30 8 20V10z"/><path d="M16 21l5 5 8-9"/></svg></div>
<div class="node" style="left:783px;top:1199px"><svg width="44" height="44" viewBox="0 0 44 44" fill="none" stroke="#fff" stroke-width="2.5"><circle cx="14" cy="14" r="6"/><rect x="18" y="20" width="20" height="16"/><path d="M18 28h20M28 20v16"/></svg></div>
<div class="node" style="left:722px;top:1354px"><svg width="44" height="44" viewBox="0 0 44 44" fill="none" stroke="#fff" stroke-width="2.5"><rect x="18" y="8" width="16" height="30" rx="2"/><path d="M27 14l-4 8h6l-4 8M10 22H4M12 12L8 8M12 32l-4 4"/></svg></div>

<div class="topic l" style="left:146px;top:1046px;width:200px"><h3>Solar Pros &amp; Cons</h3><p>Lorem ipsum dolor sit amet, consectetur adipiscing elit. Proin integer ornare consectetur sodales.Lorem ipsum dolor sit</p></div>
<div class="topic l" style="left:122px;top:1202px;width:174px"><h3>Solar Panels Home</h3><p>Lorem ipsum dolor sit amet, consectetur adipiscing elit. Proin integer ornare .Lorem ipsum dolor sit</p></div>
<div class="topic l" style="left:106px;top:1364px;width:260px"><h3>Solar Panel Cost</h3><p>Lorem ipsum dolor sit amet, consectetur adipiscing elit. Proin integer ornare consectetur sodales.Lorem ipsum dolor sit amet, consectetur adipiscing</p></div>
<div class="topic" style="left:838px;top:1043px;width:240px"><h3>Solar Rebates &amp; Incentives</h3><p>Lorem ipsum dolor sit amet, consectetur adipiscing elit. Proin integer ornare consectetur sodales.Lorem ipsum dolor sit amet, consectetur adipiscing</p></div>
<div class="topic" style="left:886px;top:1196px;width:200px"><h3>Soloar Financing</h3><p>Lorem ipsum dolor sit amet, consectetur adipiscing elit. Proin integer ornare consectetur sodales.Lorem ipsum dolor sit</p></div>
<div class="topic" style="left:830px;top:1358px;width:190px"><h3>Solar Battery</h3><p>Lorem ipsum dolor sit amet, consectetur adipiscing elit. Proin integer ornare consectetur sodales.Lorem ipsum dolor</p></div>

<svg class="abs learn-bottom" width="1092" height="113" viewBox="0 0 1092 113"><path d="M0 0 C300 55 800 55 1092 0 V113 H0Z" fill="#d4813f"/><path d="M0 0 C300 55 800 55 1092 0 V8 C800 58 300 58 0 8Z" fill="#0e1a3a" transform="translate(0,4)"/></svg>

<section class="systems">
  <div class="abs map" role="img" aria-label="World map with location markers"></div>
  <p class="abs tag-line">Solar Energy, Solar Panels, Green Energy</p>
  <h2>Connercial, Residential<br>&amp; Industrial Systems!</h2>
  <p class="abs intro">Lorem ipsum dolor sit amet, consectetur adipiscing elit. In netus dui laoreet mattis volutpat egestas faucibus. Morbi egestas ullamcorper nibh eu. Cursus aliquet egestas bibendum massa feugiat. Urna libero at arcu nam semper.</p>
  <div class="abs btn-dark">Awards &amp; Milestones <svg width="12" height="10" viewBox="0 0 12 10"><path d="M0 5h10M6 1l4 4-4 4" stroke="#fff" stroke-width="1.5" fill="none"/></svg></div>
  <div class="abs stat" style="top:333px"><b>5,874</b> <small>Project</small><br>Lorem ipsum dolor sit amet, consectetur adipiscing elit. In netus dui laoreet mattis volutpat egestas faucibus</div>
  <div class="abs stat" style="top:433px"><b>3,874</b> <small>Project</small><br>Lorem ipsum dolor sit amet, consectetur adipiscing elit. In netus dui laoreet mattis volutpat egestas faucibus</div>
</section>

<article class="card" style="left:59px">
  <p class="meta">Feb 12,2022<span>Mara Ellery</span></p>
  <h4>Filing Solar Power Permits in2022</h4>
  <p class="sub">Filing Solar Power Permits in 2022 Consider Following Important Factors</p>
  <div class="photo" role="img" aria-label="Two-storey shingled house with solar panels on the roof"></div>
  <span class="chip">Solar, Insigths</span>
  <p class="body">Lorem ipsum dolor sit amet, consectetur adipiscing elit. Sem odio vitae nibh rhoncus leo magnis. Vitae nullam id augue tellus sit. Est nunc arcu cursus convallis urna habitant enim.</p>
  <div class="more">Read More <i></i></div>
</article>
<article class="card" style="left:427px">
  <p class="meta">Feb 12,2022<span>Mara Ellery</span></p>
  <h4>Filing Solar Power Permits in2022</h4>
  <p class="sub">Filing Solar Power Permits in 2022 Consider Following Important Factors</p>
  <div class="photo wide" role="img" aria-label="Aerial view of a roof covered with solar panels among trees"></div>
  <span class="chip">Solar, Insigths</span>
  <p class="body">Lorem ipsum dolor sit amet, consectetur adipiscing elit. Sem odio vitae nibh rhoncus leo magnis. Vitae nullam id augue tellus sit. Est nunc arcu cursus convallis urna habitant enim.</p>
  <div class="more">Read More <i></i></div>
</article>
<article class="card" style="left:795px">
  <p class="meta">Feb 12,2022<span>Mara Ellery</span></p>
  <h4>Filing Solar Power Permits in2022</h4>
  <p class="sub">Filing Solar Power Permits in 2022 Consider Following Important Factors</p>
  <div class="photo" role="img" aria-label="Two-storey shingled house with solar panels on the roof"></div>
  <span class="chip">Solar, Insigths</span>
  <p class="body">Lorem ipsum dolor sit amet, consectetur adipiscing elit. Sem odio vitae nibh rhoncus leo magnis. Vitae nullam id augue tellus sit. Est nunc arcu cursus convallis urna habitant enim.</p>
  <div class="more">Read More <i></i></div>
</article>

<footer class="site-footer">
  <div class="abs brand"><span class="dot"></span>BREVANT SOLAR</div>
  <p class="abs foot-about">Lorem ipsum dolor sit amet, consectetur adipiscing elit. Varius ullamcorper metus, et, vitae dapibus aenean scelerisque elementum. Aliquam</p>
  <h5 style="left:404px">CONTACT INFO</h5>
  <p class="abs contact" style="top:98px">Address:118 Harbor Lane,<br>Sanford FL</p>
  <p class="abs contact" style="top:137px">&#9743; +1 407-555-0142</p>
  <p class="abs contact" style="top:160px">&#9993; hello@brevantsolar-example.com</p>
  <h5 style="left:684px">RECENT POSTS</h5>
  <div class="abs post" style="top:93px"><span class="thumb" style="width:44px;height:47px" role="img" aria-label="House with solar roof"></span><div><b>Sem Porta Mollis Parturi</b><small>&#9719; 21 Mar 2017</small></div></div>
  <div class="abs" style="left:738px;top:147px;width:120px;height:1px;background:#555"></div>
  <div class="abs post" style="top:164px"><span class="thumb" style="width:44px;height:47px" role="img" aria-label="House with solar roof"></span><div><b>Sem Porta Mollis Parturi</b><small>&#9719; 21 Mar 2017</small></div></div>
  <h5 style="left:979px">RECENT WORKS</h5>
  <span class="abs thumb" style="left:979px;top:93px;width:50px;height:52px" role="img" aria-label="Solar roof project"></span>
  <span class="abs thumb" style="left:1037px;top:93px;width:50px;height:52px" role="img" aria-label="Solar roof project"></span>
  <span class="abs thumb" style="left:1091px;top:93px;width:50px;height:52px" role="img" aria-label="Solar roof project"></span>
  <span class="abs thumb" style="left:979px;top:155px;width:50px;height:52px" role="img" aria-label="Solar roof project"></span>
  <span class="abs thumb" style="left:1037px;top:155px;width:50px;height:52px" role="img" aria-label="Solar roof project"></span>
  <span class="abs thumb" style="left:1091px;top:155px;width:50px;height:52px" role="img" aria-label="Solar roof project"></span>
</footer>

</body>
</html>
```